Flyer Design Project

I require a double sided flyer in PSD format.
The flyer should look fresh and clean.
The flyer is for an digital marketing company that offers various services. The services are broken down into 3 main categories and the design should reflect this.
All the content is provided in the attached file
Industry/Entity Type
Digital
Requirements
Must have
- Front of the leaflet to be mainly white background with appealing text based questions in the colours in large font with relevant images.
Back if the
3 separate boxes using the colours indicated in the attachment for the services on back of the leafet.
Should not have
- Gradients
Borders on the edges of the design
Vignettes
Black elements
Any text below 10pt
Fancy fonts
Do not use old-style fonts

```html
<!DOCTYPE html>
<html lang="en">
<head>
<meta charset="utf-8">
<title>Vantara – Services Flyer</title>
<link rel="stylesheet" href="https://fonts.googleapis.com/css2?family=Varela+Round&family=Arvo&family=Cutive&display=swap">
<style>
  :root {
    --green: #9ad35f;
    --blue: #5bcbeb;
    --orange: #ea8130;
    --white: #ffffff;
    --ink: #1e1e1e;
    --dash: #8a8a8a;
    --footer: #5a5a5a;
    --heading-font: "Varela Round", "Arial Rounded MT Bold", sans-serif;
    --body-font: "Cutive", "Arvo", serif;
  }
  * { box-sizing: border-box; margin: 0; padding: 0; }
  html, body { width: 1200px; height: 900px; overflow: hidden; background: var(--white); }
  .flyer { position: relative; width: 1200px; height: 900px; background: var(--white); }

  .service-card {
    position: absolute; top: 22px; width: 350px; height: 523px;
    border-radius: 22px; color: var(--white); padding: 40px 16px 0 26px;
  }
  .service-card--consulting { left: 29px; background: var(--green); }
  .service-card--design { left: 425px; background: var(--blue); }
  .service-card--sem { left: 819px; background: var(--orange); }

  .service-card__title {
    font-family: var(--heading-font); font-weight: 700; font-size: 54px;
    line-height: 52px; letter-spacing: 0.6px; -webkit-text-stroke: 1.6px var(--white);
    white-space: nowrap;
  }
  .service-list {
    list-style: none; margin-top: 34px; font-family: var(--body-font);
    font-size: 25px; line-height: 34px; white-space: nowrap;
  }
  .service-card--sem .service-list { margin-top: 24px; }
  .service-list li { position: relative; padding-left: 19px; }
  .service-list li::before { content: "•"; position: absolute; left: 0; }
  .service-list li .wrap { margin-left: -8px; display: inline; }

  .offer {
    position: absolute; top: 585px; width: 350px; height: 216px;
    border: 3.5px dashed var(--dash); border-radius: 22px; text-align: center;
    white-space: nowrap;
  }
  .offer--consulting { left: 29px; }
  .offer--design { left: 425px; }
  .offer--sem { left: 819px; }

  .offer__headline {
    font-family: var(--heading-font); font-weight: 700; font-size: 124px;
    line-height: 1; margin-top: 24px; letter-spacing: 0;
  }
  .offer--consulting .offer__headline { color: var(--green); -webkit-text-stroke: 3px var(--green); }
  .offer--design .offer__headline { color: var(--blue); -webkit-text-stroke: 3px var(--blue); }
  .offer--sem .offer__headline { color: var(--orange); -webkit-text-stroke: 3px var(--orange); font-size: 126px; margin-top: 24px; }

  .offer__detail { font-family: var(--body-font); color: var(--ink); font-size: 45px; line-height: 1; margin-top: -2px; }
  .offer--design .offer__detail { font-size: 66px; margin-top: -10px; }
  .offer--sem .offer__detail { font-size: 28px; line-height: 30px; margin-top: -8px; }

  .contact-line {
    position: absolute; top: 830px; left: 0; width: 1200px; text-align: center;
    font-family: var(--body-font); font-size: 20px; color: var(--footer); letter-spacing: 0.4px;
  }
  .contact-line .sep { margin: 0 9px; }
</style>
</head>
<body>
<main class="flyer">
  <section class="service-card service-card--consulting">
    <h2 class="service-card__title">Consulting<br>Services:</h2>
    <ul class="service-list">
      <li>Marketing strategy<br><span class="wrap">and planning</span></li>
      <li>Business branding</li>
      <li>Competition<br><span class="wrap">analysis</span></li>
    </ul>
  </section>

  <section class="service-card service-card--design">
    <h2 class="service-card__title">Design<br>Services:</h2>
    <ul class="service-list">
      <li>Web design</li>
      <li>Website<br><span class="wrap">maintenance</span></li>
      <li>Logo design</li>
      <li>Flyer design</li>
    </ul>
  </section>

  <section class="service-card service-card--sem">
    <h2 class="service-card__title">SEM<br>Services:</h2>
    <ul class="service-list">
      <li>Local Business<br><span class="wrap">Marketing</span></li>
      <li>PPC</li>
      <li>Email marketing</li>
      <li>SEO</li>
      <li>Social media</li>
      <li>Content<br><span class="wrap">development</span></li>
      <li>Website audit</li>
      <li>Lead generation</li>
    </ul>
  </section>

  <div class="offer offer--consulting">
    <p class="offer__headline">FREE</p>
    <p class="offer__detail">Consultation</p>
  </div>
  <div class="offer offer--design">
    <p class="offer__headline">FREE</p>
    <p class="offer__detail">Website</p>
  </div>
  <div class="offer offer--sem">
    <p class="offer__headline">25%</p>
    <p class="offer__detail">OFF any SEM<br>package</p>
  </div>

  <p class="contact-line">Vantara<span class="sep">|</span>18 Marlow Street<span class="sep">|</span>Birmingham<span class="sep">|</span>B4 7QT</p>
</main>
</body>
</html>
```